Brochure needed for 3D foam prop company

Looking for a designer to create a multi page brochure. Brochure will need to be able to be die cut so we're looking for something unique. The brochure needs to utilize our logo and the squares as possibly cut aways displaying imagery behind it for the front cover.

The brochure will feature the following sections:
- about us
- our process
- amazing clients
- anything is possible

So far we're still looking for an effective design that matches our requirements. It appears the die cutting element isn't being factored into the design (all except 1 design submitted has included this so far). Please read the brief and submit quality designs...so far we have not been very impressed.

Target Market(s)

Themeparks, water parks

Industry/Entity Type

Entertainment Industry

Font styles to use
Sans Serif

Requirements
Must have
• Logo, utilize our color theme

```html
<!DOCTYPE html>
<html lang="en">
<head>
<meta charset="utf-8">
<title>Kestrel Foam – Die-cut Brochure</title>
<link href="https://fonts.googleapis.com/css2?family=PT+Sans:wght@400;700&display=swap" rel="stylesheet">
<style>
  :root {
    --backdrop: #000000;
    --brand-blue: #0b72bb;
    --paper: #ffffff;
    --ink-light: #ffffff;
  }
  html, body {
    margin: 0;
    padding: 0;
    width: 1200px;
    height: 999px;
    overflow: hidden;
    background: var(--backdrop);
  }
  .spread {
    position: relative;
    width: 1200px;
    height: 999px;
    background: var(--backdrop);
    font-family: "PT Sans", "Myriad Pro", Arial, sans-serif;
  }
  .panel {
    position: absolute;
    top: 149px;
    height: 700px;
  }
  .panel--flap {
    width: 271px;
    background: var(--brand-blue);
    color: var(--ink-light);
  }
  .panel--left { left: 59px; }
  .panel--right { left: 870px; }
  .panel--cover {
    left: 330px;
    width: 540px;
    background: var(--paper);
  }
  .flap-copy {
    position: absolute;
    left: 14px;
    width: 239px;
  }
  .flap-copy--top { top: 24px; }
  .flap-copy--bottom { top: 572px; }
  .flap-title {
    margin: 0 0 7px;
    font-size: 15px;
    font-weight: 700;
    line-height: 18px;
  }
  .flap-text {
    margin: 0;
    font-size: 10px;
    line-height: 13px;
    text-align: justify;
  }
  .die-cuts {
    position: absolute;
    left: 0;
    top: 0;
  }
  .brand-name {
    position: absolute;
    left: 0;
    width: 540px;
    top: 406px;
    text-align: center;
    margin: 0;
    font-size: 62px;
    font-weight: 700;
    line-height: 1;
    color: var(--brand-blue);
    letter-spacing: -0.5px;
  }
</style>
</head>
<body>
<div class="spread">
  <section class="panel panel--flap panel--left">
    <div class="flap-copy flap-copy--top">
      <h2 class="flap-title">What is Lorem Ipsum?</h2>
      <p class="flap-text">Lorem Ipsum is simply dummy text of the printing and typesetting industry. Lorem Ipsum has been the industry's standard dummy text ever since the 1500s, when an unknown printer took a galley of type and scrambled it to make a type specimen book. It has survived not only five centuries, but also the leap into electronic typesetting, remaining essentially unchanged. It was popularised in the 1960s with the release of Letraset sheets containing Lorem Ipsum passages, and more recently with desktop publishing software like Aldus PageMaker including versions of Lorem Ipsum.</p>
    </div>
    <div class="flap-copy flap-copy--bottom">
      <p class="flap-text">Lorem Ipsum is simply dummy text of the printing and typesetting industry. Lorem Ipsum has been the industry's standard dummy text ever since the 1500s, when an unknown printer took a galley of type and scrambled it to make a type specimen book. It has survived not only five centuries, but also the leap into electronic typesetting, remaining essentially unchanged.</p>
    </div>
  </section>

  <section class="panel panel--cover">
    <h1 class="brand-name">Kestrel Foam</h1>
  </section>

  <section class="panel panel--flap panel--right">
    <div class="flap-copy flap-copy--top">
      <h2 class="flap-title">What is Lorem Ipsum?</h2>
      <p class="flap-text">Lorem Ipsum is simply dummy text of the printing and typesetting industry. Lorem Ipsum has been the industry's standard dummy text ever since the 1500s, when an unknown printer took a galley of type and scrambled it to make a type specimen book. It has survived not only five centuries, but also the leap into electronic typesetting, remaining essentially unchanged. It was popularised in the 1960s with the release of Letraset sheets containing Lorem Ipsum passages, and more recently with desktop publishing software like Aldus PageMaker including versions of Lorem Ipsum.</p>
    </div>
    <div class="flap-copy flap-copy--bottom">
      <p class="flap-text">Lorem Ipsum is simply dummy text of the printing and typesetting industry. Lorem Ipsum has been the industry's standard dummy text ever since the 1500s, when an unknown printer took a galley of type and scrambled it to make a type specimen book. It has survived not only five centuries, but also the leap into electronic typesetting, remaining essentially unchanged.</p>
    </div>
  </section>

  <svg class="die-cuts" width="1200" height="999" viewBox="0 0 1200 999" aria-hidden="true">
    <path d="M59 370 A226 165 0 0 1 59 700 Z" fill="var(--backdrop)"/>
    <path d="M1141 370 A226 165 0 0 0 1141 700 Z" fill="var(--backdrop)"/>
  </svg>
</div>
</body>
</html>
```